Entertainment Sound and Lighting company Business card

We need a professional looking business card designed for my growing entertainment sound and lighting company based in Sydney, Australia called "Kestrel Sound"

We provide technical production services (sound systems/lighting/vision) for events ranging from band gigs, weddings, corporate functions etc.

The business card needs to contain the following information:

Bartholomew Quenneville
Audio Engineer
Phone: 0478 615 027
Email: bartholomew@kestrelsound.com.au
Website: www.kestrelsound.com.au

Business logo has been attached in .ai format, please contact me if you need me to provide other files.

Target Market(s)

We need a business card that reflects our modern and professional company but still looks professional to appeal to our corporate clients.
We have a very broad target market spanning from bands needing PA systems for their gigs (18-30yrs) to event companies needing sound and lighting for weddings and other functions.

Industry/Entity Type

Business

Requirements
Must have
• Needs to include the logo that is attached of course, and the colour scheme.
Nice to have
• - Double sided

```html
<!DOCTYPE html>
<html lang="en">
<head>
<meta charset="utf-8">
<title>Kestrel Sound — Business Card</title>
<link rel="stylesheet" href="https://fonts.googleapis.com/css2?family=EB+Garamond:ital,wght@0,500;1,400&display=swap">
<style>
  :root {
    --cyan: #00b9e4;
    --cyan-text: #10a9df;
    --white: #ffffff;
    --divider: #000000;
  }
  * { margin: 0; padding: 0; box-sizing: border-box; }
  html, body { width: 1056px; height: 1200px; overflow: hidden; background: var(--white); }
  .sheet { position: relative; width: 1056px; height: 1200px; }
  .card-face { position: absolute; left: 0; width: 1056px; height: 600px; overflow: hidden; }
  .card-front { top: 0; background: var(--white); }
  .card-back { top: 600px; background: var(--cyan); border-top: 2px solid var(--divider); }
  .tabs { position: absolute; inset: 0; width: 100%; height: 100%; }
  .brand-name {
    position: absolute; left: 0; right: 0; text-align: center;
    font-family: "EB Garamond", Georgia, serif; font-weight: 500; letter-spacing: 1px;
  }
  .card-front .brand-name { top: 246px; font-size: 84px; color: var(--cyan-text); }
  .card-back .brand-name { top: 166px; font-size: 62px; color: var(--white); }
  .rule { position: absolute; height: 3px; }
  .card-front .rule {
    top: 383px; left: 205px; width: 646px;
    background: linear-gradient(90deg, rgba(0,185,228,0), rgba(0,185,228,0.75) 50%, rgba(0,185,228,0));
  }
  .card-back .rule {
    top: 282px; left: 225px; width: 645px;
    background: linear-gradient(90deg, rgba(255,255,255,0), rgba(255,255,255,0.8) 50%, rgba(255,255,255,0));
  }
  .holder-name {
    position: absolute; top: 413px; left: 0; right: 0; text-align: center;
    font-family: "EB Garamond", Georgia, serif; font-style: italic; font-size: 33px; color: var(--cyan-text);
  }
  .contact {
    position: absolute; top: 310px; left: 0; right: 0; text-align: center; list-style: none;
    font-family: "EB Garamond", Georgia, serif; font-style: italic; font-size: 34px; line-height: 48px; color: var(--white);
  }
</style>
</head>
<body>
<main class="sheet">
  <section class="card-face card-front">
    <svg class="tabs" viewBox="0 0 1056 600" aria-hidden="true">
      <path d="M265 0 H805 L785 27 Q535 4 285 27 Z" fill="var(--cyan)"/>
      <path d="M265 600 H805 L785 573 Q535 596 285 573 Z" fill="var(--cyan)"/>
    </svg>
    <h1 class="brand-name">Kestrel Sound</h1>
    <div class="rule"></div>
    <p class="holder-name">Bartholomew Quenneville</p>
  </section>

  <section class="card-face card-back">
    <svg class="tabs" viewBox="0 0 1056 600" aria-hidden="true">
      <path d="M265 -2 H805 L785 25 Q535 2 285 25 Z" fill="var(--white)"/>
      <path d="M265 600 H805 L785 572 Q535 595 285 572 Z" fill="var(--white)"/>
    </svg>
    <h2 class="brand-name">Kestrel Sound</h2>
    <div class="rule"></div>
    <ul class="contact">
      <li>Bartholomew Quenneville</li>
      <li>Audio Engineer</li>
      <li>Phone: 0478 615 027</li>
      <li>Email: bartholomew@kestrelsound.com.au</li>
      <li>Website: www.kestrelsound.com.au</li>
    </ul>
  </section>
</main>
</body>
</html>
```